Designing of Orientation Materials and Innovative Ways to ‘Market’ Procurement Function

To Market and promote Procurement function and it’s ‘real’ capabilities clearly, to demonstrate that the function is an enabler instead being perceive as a barrier to other internal functions. Sometimes due to the lack of a common language even makes it difficult for other functions (e.g) Marketing and Procurement to understand each other’s aims and intentions.
The audience could be from all functions such as; Human Resource, Finance, Sales & Marketing, Supply Chain/Procurement, Corporate Affairs and Information System.

```html
<!DOCTYPE html>
<html lang="en">
<head>
<meta charset="utf-8">
<title>Procurement's Evolving Value Proposition</title>
<link rel="stylesheet" href="https://fonts.googleapis.com/css2?family=Fira+Sans:wght@600;700&display=swap">
<style>
  :root {
    --brand-blue: #1173bd;
    --line-blue: #1a7cc1;
    --paper: #ffffff;
    --stage: #eef1f4;
    --text-light: #ffffff;
    --text-blue: #1877bf;
  }
  html, body {
    margin: 0;
    width: 1200px;
    height: 1200px;
    overflow: hidden;
    background: var(--stage);
  }
  .poster {
    position: absolute;
    left: 0;
    top: 232px;
    width: 1200px;
    height: 735px;
    box-shadow: 0 10px 24px rgba(0,0,0,0.25);
    background: var(--paper);
  }
  .poster svg { display: block; width: 100%; height: 100%; }
  .poster text { font-family: "Fira Sans", Arial, sans-serif; font-weight: 700; }
  .title { fill: var(--text-light); font-size: 34px; letter-spacing: 0.5px; }
  .column-head { font-size: 24px; }
  .column-head--left { fill: var(--text-light); }
  .column-head--right { fill: var(--text-blue); }
  .role-label { fill: var(--text-light); font-size: 15px; font-weight: 600; }
  .value-label { fill: var(--text-blue); font-size: 15px; font-weight: 600; }
  .tier-label { fill: var(--text-light); font-size: 23px; letter-spacing: 0.5px; }
  .blue-field { fill: var(--brand-blue); }
  .role-line { stroke: var(--text-light); stroke-width: 1.6; fill: none; }
  .role-dot { fill: var(--text-light); }
  .value-line { stroke: var(--line-blue); stroke-width: 1.6; fill: none; }
  .value-dot { fill: var(--line-blue); }
  .tier-shadow { fill: rgba(200,210,220,0.25); }
</style>
</head>
<body>
<div class="poster">
<svg viewBox="0 0 1316 806" xmlns="http://www.w3.org/2000/svg">
  <defs>
    <linearGradient id="tier-value" x1="0" y1="0" x2="0" y2="1">
      <stop offset="0" stop-color="#f7861c"/><stop offset="1" stop-color="#e2c63c"/>
    </linearGradient>
    <linearGradient id="tier-demand" x1="0" y1="0" x2="1" y2="0">
      <stop offset="0" stop-color="#8cc63f"/><stop offset="1" stop-color="#5db94f"/>
    </linearGradient>
    <linearGradient id="tier-tco" x1="0" y1="0" x2="1" y2="0">
      <stop offset="0" stop-color="#55b96c"/><stop offset="1" stop-color="#3cb59a"/>
    </linearGradient>
    <linearGradient id="tier-price" x1="0" y1="0" x2="1" y2="0">
      <stop offset="0" stop-color="#25b4ae"/><stop offset="1" stop-color="#17a9c2"/>
    </linearGradient>
    <linearGradient id="tier-supply" x1="0" y1="0" x2="1" y2="0">
      <stop offset="0" stop-color="#1ca3c6"/><stop offset="1" stop-color="#1d88c8"/>
    </linearGradient>
  </defs>

  <!-- split background -->
  <rect class="blue-field" x="0" y="0" width="662" height="806"/>

  <!-- title band -->
  <rect class="blue-field" x="300" y="34" width="776" height="56" rx="16"/>
  <text class="title" x="665" y="76" text-anchor="middle">PROCUREMENT’S EVOLVING VALUE PROPOSITION</text>

  <text class="column-head column-head--left" x="316" y="144" text-anchor="middle">ROLE OF PROCUREMENT</text>
  <text class="column-head column-head--right" x="1011" y="144" text-anchor="middle">VALUE PROPOSITION</text>

  <!-- pyramid gaps -->
  <polygon class="tier-shadow" points="554,317 774,317 825,354 531,354"/>
  <polygon class="tier-shadow" points="493,420 833,420 862,458 470,458"/>
  <polygon class="tier-shadow" points="432,524 894,524 924,562 402,562"/>
  <polygon class="tier-shadow" points="362,636 964,636 990,674 336,674"/>

  <!-- pyramid tiers -->
  <polygon points="663,126 774,317 554,317" fill="url(#tier-value)"/>
  <text class="tier-label" x="663" y="266" text-anchor="middle">VALUE</text>
  <text class="tier-label" x="663" y="296" text-anchor="middle">MANAGEMENT</text>

  <polygon points="531,354 795,354 833,420 493,420" fill="url(#tier-demand)"/>
  <text class="tier-label" x="665" y="396" text-anchor="middle">DEMAND MANAGEMENT</text>

  <polygon points="470,458 856,458 894,524 432,524" fill="url(#tier-tco)"/>
  <text class="tier-label" x="663" y="500" text-anchor="middle">TOTAL COST OF OWNERSHIP</text>

  <polygon points="410,562 916,562 958,636 368,636" fill="url(#tier-price)"/>
  <text class="tier-label" x="665" y="608" text-anchor="middle">PRICE</text>

  <polygon points="345,674 980,674 1022,748 304,748" fill="url(#tier-supply)"/>
  <text class="tier-label" x="665" y="720" text-anchor="middle">SUPPLY ASSURANCE</text>

  <!-- role connector -->
  <polyline class="role-line" points="568,231 483,376 424,477 349,608 293,704"/>
  <circle class="role-dot" cx="568" cy="231" r="7"/>
  <circle class="role-dot" cx="483" cy="376" r="7"/>
  <circle class="role-dot" cx="424" cy="477" r="7"/>
  <circle class="role-dot" cx="349" cy="608" r="7"/>
  <circle class="role-dot" cx="293" cy="704" r="7"/>

  <text class="role-label" x="542" y="236" text-anchor="end">INCREASE BUSINESS VALUE DERIVED FROM SPEND</text>
  <text class="role-label" x="456" y="371" text-anchor="end">REDUCE DEMAND ACTIVITY, COMPLEXITY</text>
  <text class="role-label" x="456" y="390" text-anchor="end">AND VARIABILITY</text>
  <text class="role-label" x="398" y="482" text-anchor="end">SHIFT FROM LOWEST PRICE TO TCO</text>
  <text class="role-label" x="320" y="603" text-anchor="end">RIGHT GOODS AND SERVICES</text>
  <text class="role-label" x="320" y="622" text-anchor="end">AT THE RIGHT PRICE</text>
  <text class="role-label" x="267" y="700" text-anchor="end">RIGHT GOODS /SERVICES AT</text>
  <text class="role-label" x="267" y="719" text-anchor="end">THE RIGHT TIME AND PLACE</text>

  <!-- value connector -->
  <polyline class="value-line" points="762,231 848,376 907,477 982,608 1038,704"/>
  <circle class="value-dot" cx="762" cy="231" r="7"/>
  <circle class="value-dot" cx="848" cy="376" r="7"/>
  <circle class="value-dot" cx="907" cy="477" r="7"/>
  <circle class="value-dot" cx="982" cy="608" r="7"/>
  <circle class="value-dot" cx="1038" cy="704" r="7"/>

  <text class="value-label" x="780" y="236">TRUSTED BUSINESS ADVISOR AND CHANGE AGENT</text>
  <text class="value-label" x="871" y="370">SPEND/ BUDGET CONSULTANT AND</text>
  <text class="value-label" x="871" y="389">RELATIONSHIP MANAGER</text>
  <text class="value-label" x="931" y="471">SUPPLY EXPERT, TEAM LEADER,</text>
  <text class="value-label" x="931" y="490">PROJECT MANAGER</text>
  <text class="value-label" x="1007" y="612">NEGOTIATOR</text>
  <text class="value-label" x="1062" y="709">BUYER/PLANNER</text>
</svg>
</div>
</body>
</html>
```